R&T Promotions / P.L.W. Sales Business Cards

I have 2 companies that are somewhat connected, yet sell to 2 different markets.

R&T Promotions www.rotapfx.example

We are a manufacturers representative company. We handle sales and marketing of Home Theater, Home Automation, Audio & Video products for the state of Florida. We work with Designers, Architects, Technology Consultants and Electronic Integrators to design, sell and install cutting edge technology in new and existing homes, condos and commercial spaces.

P.L.W. Sales www.plwqz.example

We are a manufacturers representative company. We handle sales and marketing of automotive Audio, Electronics, Security, Navigation and Entertainment products for the state of Florida. We work with 12-volt retailers, installers and automobile customizers to design, sell, merchandise, fabricate and install cutting edge technology in cars, boats, motor coaches, etc.

We have logo's that might still be relevant, but might need a little touching up. We need a new business card design and layout for each of the 2 companies. I would like them to have a family look, but still better speak to the customer base associated with the channel.

Target Market(s)

R&T Promotions -

Design, Engineering, Construction, Technology, elegant, tasteful.

P.L.W. Sales -

More cutting edge, industrial, youth, aggressive, fun, bold.

Industry/Entity Type

Business

Requirements
Must have
• New business card layout for both companies.
Nice to have
• A family look, or relationship to the other company. Even if it's just a logo referencing the other company.

```html
<!DOCTYPE html>
<html lang="en">
<head>
<meta charset="utf-8">
<title>P.L.W. Sales Business Card</title>
<link href="https://fonts.googleapis.com/css2?family=Cinzel:wght@400;700&display=swap" rel="stylesheet">
<style>
  :root {
    --page-bg: #e4e4e4;
    --card-top: #f1f2f3;
    --card-mid: #eceded;
    --card-bottom: #b9b9b9;
    --ink: #1a1a1a;
    --rule: #555555;
  }
  html, body {
    margin: 0;
    padding: 0;
    width: 1200px;
    height: 1000px;
    overflow: hidden;
    background: var(--page-bg);
  }
  .canvas {
    position: relative;
    width: 1200px;
    height: 1000px;
  }
  .business-card {
    position: absolute;
    left: 100px;
    top: 214px;
    width: 1000px;
    height: 572px;
    border-radius: 26px;
    background: linear-gradient(180deg, var(--card-top) 0%, var(--card-mid) 62%, var(--card-bottom) 100%);
    box-shadow: 0 6px 18px rgba(0,0,0,0.18);
    font-family: "Cinzel", "Times New Roman", serif;
    color: var(--ink);
  }
  .name-block {
    position: absolute;
    left: 150px;
    top: 92px;
    width: 280px;
    text-align: center;
  }
  .person-name {
    font-size: 27px;
    letter-spacing: 1px;
    line-height: 1.1;
  }
  .person-title {
    font-size: 19px;
    line-height: 1.1;
  }
  .name-rule {
    margin-top: 12px;
    border: 0;
    border-top: 1.5px solid var(--rule);
  }
  .contact-list {
    position: absolute;
    left: 110px;
    top: 225px;
    margin: 0;
    padding: 0;
    list-style: none;
    font-size: 22px;
    line-height: 34px;
  }
  .contact-list li:nth-child(2) { padding-left: 14px; }
  .contact-list li:nth-child(3) { padding-left: 28px; }
  .contact-list li:nth-child(4) { padding-left: 42px; }
  .contact-list li:nth-child(5) { padding-left: 56px; font-size: 20px; }
  .contact-list li:nth-child(6) { padding-left: 70px; font-size: 20px; }
  .brand-name {
    position: absolute;
    left: 540px;
    top: 80px;
    width: 420px;
    text-align: center;
    font-weight: 700;
    line-height: 0.95;
  }
  .brand-name .brand-top { display: block; font-size: 108px; letter-spacing: 2px; }
  .brand-name .brand-bottom { display: block; font-size: 92px; letter-spacing: 4px; }
  .partner-row {
    position: absolute;
    left: 620px;
    top: 330px;
    display: flex;
    gap: 34px;
    align-items: center;
  }
  .partner-name {
    font-size: 20px;
    font-weight: 700;
    line-height: 1;
  }
</style>
</head>
<body>
<main class="canvas">
  <section class="business-card" aria-label="P.L.W. Sales business card">
    <div class="name-block">
      <div class="person-name">Dale Morrow</div>
      <div class="person-title">Rep Principle</div>
      <hr class="name-rule">
    </div>

    <ul class="contact-list">
      <li>2261 NW 41st Avenue</li>
      <li>Ocala, FL 34482</li>
      <li>Tel. 800-555-0148</li>
      <li>Fax. 305-555-0193</li>
      <li>dale@plw-rt.example</li>
      <li>http://www.plw-rt.example</li>
    </ul>

    <div class="brand-name">
      <span class="brand-top">P.L.W.</span>
      <span class="brand-bottom">SALES</span>
    </div>

    <div class="partner-row">
      <span class="partner-name">R&amp;T Promotions</span>
      <span class="partner-name">Q.V.N. Supply</span>
    </div>
  </section>
</main>
</body>
</html>
```